Business Card Design Project

Thornwick Property Management

Our Business is residential property management, we therefore need a card that displays a professional image, but is clear and concise, and easy to read
Updates

We are committed now guys and girls, loving what we are seeing so far! 

Target Market(s)

Landlords, Rental Property Owners

Industry/Entity Type

Residential

Requirements
Must have
• Dale Thornwick - Principal
Fiona Thornwick - Director (Property Management)

PO Box 817
Pellworth SA 5193

Dale: 0490 367 258
Fiona: 0490 723 519

www.thornwickpropertymanagement.com.au
admin@thornwickpropertymanagement.com.au

Nice to have
• I would like the card to be double sided, white background on the information side and then colour on the reverse, in blue or black and incorporating our logo

```html
<!DOCTYPE html>
<html lang="en">
<head>
<meta charset="utf-8">
<title>Thornwick Property Management – Business Card</title>
<link rel="stylesheet" href="https://fonts.googleapis.com/css2?family=Arimo:wght@400;700&display=swap">
<style>
  :root {
    --page-bg: #eef0f2;
    --brand-blue-light: #5cb1e5;
    --brand-blue: #3e98d7;
    --brand-blue-deep: #2a7fc0;
    --ink-dark: #3b3b3d;
    --ink-mid: #5a5a5c;
    --white: #ffffff;
  }
  * { box-sizing: border-box; margin: 0; padding: 0; }
  html, body {
    width: 1157px;
    height: 1200px;
    overflow: hidden;
    background: var(--page-bg);
    font-family: "Arimo", Arial, sans-serif;
  }
  .canvas {
    position: relative;
    width: 1157px;
    height: 1200px;
  }
  .card {
    position: absolute;
    left: 246px;
    width: 665px;
    height: 412px;
    overflow: hidden;
    box-shadow: 0 6px 18px rgba(0,0,0,0.18);
  }
  /* Front */
  .card-front {
    top: 110px;
    background: linear-gradient(135deg, var(--brand-blue-light) 0%, var(--brand-blue) 100%);
    display: flex;
    align-items: center;
    justify-content: center;
  }
  .brand-lockup {
    display: flex;
    align-items: center;
    gap: 22px;
    color: var(--ink-dark);
    font-weight: 700;
  }
  .brand-square {
    width: 64px;
    height: 64px;
    background: var(--brand-blue-deep);
    flex: none;
  }
  .brand-name { line-height: 1; }
  .brand-name .primary { display: block; font-size: 62px; letter-spacing: -0.5px; }
  .brand-name .secondary { display: block; font-size: 24px; margin-top: 8px; }

  /* Back */
  .card-back {
    top: 600px;
    background: var(--white);
  }
  .back-band {
    position: absolute;
    left: 0; top: 0;
    width: 100%;
    height: 246px;
    background: linear-gradient(135deg, var(--brand-blue-light) 0%, var(--brand-blue) 100%);
    color: var(--white);
    font-size: 19px;
  }
  .postal {
    position: absolute;
    left: 61px;
    top: 92px;
    line-height: 24px;
  }
  .online {
    position: absolute;
    left: 61px;
    top: 172px;
    list-style: none;
    line-height: 24px;
  }
  .online li { display: flex; align-items: center; gap: 9px; }
  .icon { width: 15px; height: 15px; flex: none; }
  .people {
    position: absolute;
    left: 61px;
    right: 62px;
    top: 276px;
    display: flex;
    justify-content: space-between;
    font-size: 19px;
  }
  .person { line-height: 24px; }
  .person-right { text-align: right; }
  .person .name { color: var(--ink-mid); }
  .person .role { color: var(--brand-blue); }
  .person .phone {
    margin-top: 17px;
    color: var(--ink-dark);
    display: flex;
    align-items: center;
    gap: 8px;
  }
  .person-right .phone { justify-content: flex-end; }
  .phone .icon { width: 14px; height: 14px; }
</style>
</head>
<body>
<main class="canvas">

  <section class="card card-front" aria-label="Card front">
    <div class="brand-lockup">
      <span class="brand-square" aria-hidden="true"></span>
      <h1 class="brand-name">
        <span class="primary">Thornwick</span>
        <span class="secondary">Property Management</span>
      </h1>
    </div>
  </section>

  <section class="card card-back" aria-label="Card back">
    <div class="back-band">
      <address class="postal" style="font-style:normal">
        PO Box 817<br>Pellworth SA 5193
      </address>
      <ul class="online">
        <li>
          <svg class="icon" viewBox="0 0 16 16" aria-hidden="true" fill="none" stroke="#fff" stroke-width="1.4">
            <circle cx="8" cy="8" r="6.5"/>
            <ellipse cx="8" cy="8" rx="3" ry="6.5"/>
            <line x1="1.5" y1="8" x2="14.5" y2="8"/>
          </svg>
          www.thornwickpropertymanagement.com.au
        </li>
        <li>
          <svg class="icon" viewBox="0 0 16 16" aria-hidden="true">
            <rect x="1" y="3" width="14" height="10" fill="#fff"/>
            <polyline points="1,3 8,9 15,3" fill="none" stroke="#3e98d7" stroke-width="1.3"/>
          </svg>
          admin@thornwickpropertymanagement.com.au
        </li>
      </ul>
    </div>

    <div class="people">
      <div class="person person-left">
        <p class="name">Dale Thornwick</p>
        <p class="role">Principal</p>
        <p class="phone">
          <svg class="icon" viewBox="0 0 16 16" aria-hidden="true"><path fill="#3e98d7" d="M3.6 1.2l2.3 2.6-1.3 1.8c.9 2 2.4 3.6 4.4 4.6l1.8-1.3 2.6 2.3-1.4 2.4C6.6 13.2 2.8 9.4 1.2 4z"/></svg>
          0490 367 258
        </p>
      </div>
      <div class="person person-right">
        <p class="name">Fiona Thornwick</p>
        <p class="role">Director (Property Management)</p>
        <p class="phone">
          <svg class="icon" viewBox="0 0 16 16" aria-hidden="true"><path fill="#3e98d7" d="M3.6 1.2l2.3 2.6-1.3 1.8c.9 2 2.4 3.6 4.4 4.6l1.8-1.3 2.6 2.3-1.4 2.4C6.6 13.2 2.8 9.4 1.2 4z"/></svg>
          0490 723 519
        </p>
      </div>
    </div>
  </section>

</main>
</body>
</html>
```